brivox new business card design project

we need a new business card design. you can view info about us @ brivox.com. i have attached an example of our previous card with our previous name that we no longer use. We really liked the design, colors etc. look below to see more info about this project. it asks for a limited number of words. please see our website for more info about our compnay.

Target Market(s)

law enforcement

Contact Information for Business Card

i have uploaded an example of what we used before that we liked.

Font styles to use
Serif

```html
<!DOCTYPE html>
<html lang="en">
<head>
<meta charset="utf-8">
<title>Brivox Business Card</title>
<link rel="stylesheet" href="https://fonts.googleapis.com/css2?family=Caladea:wght@400;700&display=swap">
<style>
  :root {
    --page-bg: #d9dadc;
    --card-deep: #050b16;
    --card-mid: #0c1a2e;
    --card-glow: #12294a;
    --ink-light: #f2f4f7;
    --ink-soft: #c9ced6;
    --rule: #8a93a1;
  }
  * { margin: 0; padding: 0; box-sizing: border-box; }
  html, body {
    width: 1200px; height: 1200px; overflow: hidden;
    background: var(--page-bg);
  }
  .canvas {
    position: relative; width: 1200px; height: 1200px;
    display: flex; flex-direction: column; align-items: center; justify-content: center;
    gap: 70px;
    font-family: "Caladea", Georgia, serif;
  }
  .card {
    position: relative; width: 720px; height: 411px;
    border-radius: 4px; overflow: hidden;
    box-shadow: 0 10px 30px rgba(0,0,0,0.25);
  }
  .card-texture {
    position: absolute; inset: 0;
    background:
      radial-gradient(ellipse at 70% 30%, var(--card-glow) 0%, transparent 55%),
      radial-gradient(ellipse at 25% 80%, #0e2240 0%, transparent 50%),
      linear-gradient(160deg, var(--card-mid) 0%, var(--card-deep) 100%);
  }
  .card-front .brand-name {
    position: absolute; inset: 0;
    display: flex; align-items: center; justify-content: center;
    font-size: 92px; font-weight: 400; letter-spacing: 10px;
    color: var(--ink-light);
  }
  .card-back .contact-block {
    position: absolute; inset: 0;
    display: flex; flex-direction: column; align-items: center; justify-content: center;
    color: var(--ink-light); text-align: center;
  }
  .person-name { font-size: 34px; letter-spacing: 1.5px; line-height: 1; }
  .person-title { font-size: 17px; color: var(--ink-soft); margin-top: 8px; }
  .divider-mark { margin: 18px 0 10px; }
  .rule { width: 430px; height: 1px; background: var(--rule); }
  .contact-lines { padding: 16px 0; font-size: 21px; line-height: 1.45; }
  .address { padding-top: 14px; font-size: 23px; letter-spacing: 0.3px; }
</style>
</head>
<body>
<main class="canvas">
  <section class="card card-front">
    <div class="card-texture" role="img" aria-label="Dark navy network-node pattern background"></div>
    <div class="brand-name">BRIVOX</div>
  </section>

  <section class="card card-back">
    <div class="card-texture" role="img" aria-label="Dark navy network-node pattern background"></div>
    <div class="contact-block">
      <div class="person-name">DANIEL REYES</div>
      <div class="person-title">Creative Designer</div>
      <svg class="divider-mark" width="14" height="14" viewBox="0 0 14 14" aria-hidden="true">
        <rect x="1" y="1" width="12" height="12" fill="none" stroke="#c9ced6" stroke-width="1.2"/>
      </svg>
      <div class="rule"></div>
      <div class="contact-lines">
        <div class="phone">866.555.0142</div>
        <div class="web">info@brivox.com | www.brivox.com</div>
      </div>
      <div class="rule"></div>
      <div class="address">4120 Larkspur Avenue, Austin, TX 78701</div>
    </div>
  </section>
</main>
</body>
</html>
```